Fahrzeugbeschriftung für Unternehmen im Bereich der Glasfaser-Montage
Zielgruppe
Wir sind im Bereich der Glasfaser-Montage tätig,
einblasen von Glasfaser Kabel, herstellen von LWL Splicen
Tätigkeitsstichworte:
LWL Einblasarbeiten
LWL Splicearbeiten
Entstörungsservice
Druckprüfunge Flowkarohre
Aufgabenstellung
Die Beschriftung muss sich an der vorhandenen KFZ Beschriftung der Wendt Elektro GmbH orientieren, da
wir uns mit dieser Firmen zusammen schließen werden.

```html
<!DOCTYPE html>
<html lang="de">
<head>
<meta charset="utf-8">
<title>Fahrzeugbeschriftung Wendt Elektro</title>
<link rel="stylesheet" href="https://fonts.googleapis.com/css2?family=Arimo:wght@400;700&display=swap">
<style>
  :root {
    --paper: #ffffff;
    --ink: #1d1d1b;
    --brand-green: #00b48c;
    --body-grey: #a4a5a8;
    --glass: #dcdde0;
    --frame-grey: #9fa0a3;
    --tyre: #231f20;
    --rim: #d6d7d9;
    --light-red: #d3262b;
    --line-soft: #c9cacc;
  }
  html, body { margin: 0; padding: 0; overflow: hidden; background: var(--paper); }
  .canvas { width: 1200px; height: 1200px; display: block; }
  .van-outline { fill: var(--paper); stroke: var(--ink); stroke-width: 3; }
  .bumper { fill: var(--body-grey); stroke: var(--ink); stroke-width: 2; }
  .window-frame { fill: var(--frame-grey); stroke: var(--ink); stroke-width: 2; }
  .window-glass { fill: var(--glass); stroke: var(--ink); stroke-width: 1.5; }
  .panel-line { fill: none; stroke: var(--ink); stroke-width: 1.5; }
  .soft-line { fill: none; stroke: var(--line-soft); stroke-width: 1.5; }
  .handle { fill: var(--frame-grey); stroke: var(--ink); stroke-width: 2; }
  .tail-light { fill: var(--light-red); stroke: var(--ink); stroke-width: 2; }
  .head-light { fill: var(--glass); stroke: var(--ink); stroke-width: 2; }
  .tyre { fill: var(--tyre); }
  .rim { fill: var(--rim); stroke: var(--ink); stroke-width: 2; }
  .hub { fill: var(--body-grey); stroke: var(--ink); stroke-width: 2; }
  .arch { fill: none; stroke: var(--tyre); stroke-width: 14; }
  .stripe-green { fill: var(--brand-green); }
  .stripe-black { fill: var(--ink); }
  .brand-name { font-family: "Arimo", Arial, sans-serif; font-weight: 700; fill: var(--brand-green); }
  .service-list { font-family: "Arimo", Arial, sans-serif; font-weight: 700; fill: var(--ink); }
  .contact { font-family: "Arimo", Arial, sans-serif; font-weight: 700; fill: var(--ink); letter-spacing: -0.3px; }
</style>
</head>
<body>
<svg class="canvas" viewBox="0 0 1920 1920" xmlns="http://www.w3.org/2000/svg">
  <defs>
    <path id="van-body-shape" d="M240,600 L245,545 Q255,420 280,340 Q300,328 420,326 L1100,326 Q1280,335 1330,360 L1530,505 L1575,510 Q1700,560 1740,600 L1765,680 L1775,780 Q1770,800 1700,805 L1628,812 A120 120 0 0 0 1388,815 L630,815 A120 120 0 0 0 390,815 L220,805 L218,770 L235,745 L240,690 Z"/>

    <g id="wheel">
      <circle class="tyre" r="113"/>
      <circle class="rim" r="74"/>
      <circle class="hub" r="36"/>
      <circle fill="none" stroke="var(--ink)" stroke-width="2" r="60"/>
    </g>

    <g id="van-body">
      <use href="#van-body-shape" class="van-outline"/>
      <path class="bumper" d="M255,600 L300,600 L302,745 L240,745 L218,770 L220,805 L390,815 L395,745 L255,740 Z"/>
      <path class="bumper" d="M1590,700 Q1620,660 1650,650 L1765,665 L1775,780 Q1770,800 1700,805 L1628,812 Q1620,740 1590,700 Z"/>
      <path class="window-frame" d="M765,362 L1085,362 Q1093,362 1093,372 L1093,525 Q1093,533 1085,533 L765,533 Z"/>
      <rect class="window-glass" x="777" y="377" width="307" height="137" rx="6"/>
      <path class="window-glass" d="M1130,372 L1250,376 Q1300,380 1360,430 L1440,510 Q1445,540 1435,545 L1150,535 Z"/>
      <path class="window-frame" d="M1325,480 Q1340,460 1380,470 Q1410,490 1418,515 Q1400,530 1365,530 L1325,520 Z"/>
      <path class="window-glass" d="M1330,365 L1345,360 L1530,505 L1510,510 Z"/>
      <path class="panel-line" d="M763,362 L763,805 M1108,352 L1110,805 M1435,545 L1435,700"/>
      <path class="panel-line" d="M300,585 L763,588 M763,583 L1435,585"/>
      <path class="soft-line" d="M640,760 L1365,760 M300,605 L763,605 M1110,612 L1600,615"/>
      <path class="soft-line" d="M370,745 Q400,645 510,642 Q620,645 640,760 M1365,760 Q1390,650 1505,645 Q1600,650 1635,720"/>
      <rect class="handle" x="1018" y="557" width="62" height="10" rx="5"/>
      <rect class="handle" x="1135" y="557" width="62" height="10" rx="5"/>
      <rect class="tail-light" x="256" y="578" width="46" height="92" rx="6"/>
      <path class="head-light" d="M1602,592 L1745,605 Q1760,630 1755,660 L1640,650 Q1610,620 1602,592 Z"/>
      <path class="panel-line" d="M1690,700 L1765,700 L1765,740 L1690,740 Z M1690,710 L1765,710 M1690,720 L1765,720 M1690,730 L1765,730"/>
      <path class="arch" d="M400,815 A110 110 0 0 1 620,815"/>
      <path class="arch" d="M1398,815 A110 110 0 0 1 1618,815"/>
      <use href="#wheel" x="510" y="795"/>
      <use href="#wheel" x="1508" y="795"/>
    </g>

    <clipPath id="clip-van-right">
      <use href="#van-body-shape"/>
    </clipPath>
    <clipPath id="clip-van-left">
      <use href="#van-body-shape" transform="translate(1990,760) scale(-1,1)"/>
    </clipPath>

    <linearGradient id="fibre-glow" x1="0" y1="1" x2="1" y2="0">
      <stop offset="0" stop-color="#050308"/>
      <stop offset="0.35" stop-color="#3a3670"/>
      <stop offset="0.55" stop-color="#7c7cc2"/>
      <stop offset="0.75" stop-color="#26224a"/>
      <stop offset="1" stop-color="#050308"/>
    </linearGradient>
  </defs>

  <!-- Fahrzeug rechts fahrend -->
  <g class="vehicle vehicle-right">
    <use href="#van-body"/>
    <g class="wrap" clip-path="url(#clip-van-right)">
      <polygon fill="#9a9590" role="img" aria-label="Foto: Hände beim Einziehen von Glasfaser-Leerrohren" points="240,326 780,326 240,540"/>
      <polygon class="stripe-black" points="780,326 800,326 240,548 240,540"/>
      <polygon class="stripe-green" points="800,326 840,326 240,580 240,548"/>
      <polygon class="stripe-green" points="240,345 420,326 430,326 240,360"/>
    </g>
    <use href="#van-body-shape" fill="none" stroke="var(--ink)" stroke-width="3"/>
    <text class="brand-name" x="368" y="640" font-size="56">Wendt Elektro</text>
    <text class="service-list" font-size="20">
      <tspan x="848" y="650">Elektrotechnik</tspan>
      <tspan x="848" y="677">Installation</tspan>
      <tspan x="848" y="704">Kundendienst</tspan>
      <tspan x="848" y="731">Gebäudesystemtechnik</tspan>
    </text>
    <text class="contact" font-size="14">
      <tspan x="1202" y="645">54321 Seehafen</tspan>
      <tspan x="1202" y="663">01234 - 5678</tspan>
      <tspan x="1202" y="681">www.wendt-elektro.de</tspan>
    </text>
  </g>

  <!-- Fahrzeug links fahrend -->
  <g class="vehicle vehicle-left">
    <use href="#van-body" transform="translate(1990,760) scale(-1,1)"/>
    <g class="wrap" clip-path="url(#clip-van-left)">
      <rect fill="var(--paper)" x="895" y="1115" width="330" height="175" stroke="var(--line-soft)" stroke-width="2" rx="8"/>
      <polygon fill="url(#fibre-glow)" role="img" aria-label="Foto: leuchtende Glasfaser vor dunklem Hintergrund" points="590,1505 1500,1080 1780,1080 1780,1240 1040,1580 590,1580"/>
      <polygon class="stripe-green" points="570,1478 1445,1075 1485,1075 582,1495"/>
      <polygon class="stripe-black" points="582,1495 1485,1075 1505,1075 590,1505"/>
      <polygon class="stripe-black" points="1040,1580 1780,1240 1780,1255 1068,1580"/>
      <polygon class="stripe-green" points="1068,1580 1780,1255 1780,1280 1110,1580"/>
    </g>
    <use href="#van-body-shape" transform="translate(1990,760) scale(-1,1)" fill="none" stroke="var(--ink)" stroke-width="3"/>
    <text class="brand-name" x="910" y="1180" font-size="32">Wendt Elektro</text>
    <text class="service-list" font-size="14">
      <tspan x="582" y="1340">Elektrotechnik</tspan>
      <tspan x="582" y="1359">Installation</tspan>
      <tspan x="582" y="1378">Kundendienst</tspan>
      <tspan x="582" y="1397">Gebäudesystemtechnik</tspan>
    </text>
    <text class="contact" font-size="12">
      <tspan x="1562" y="1400">54321 Seehafen</tspan>
      <tspan x="1562" y="1415">01234 - 5678</tspan>
      <tspan x="1562" y="1430">www.wendt-elektro.de</tspan>
    </text>
  </g>
</svg>
</body>
</html>
```